“Bright Tide” Spring Fair Poster

We are putting together a school and community fair. We need a poster designed to advertise the event and give some important information to would be attendees. We’d like the poster graphics to evoke a minimalistic and futuristic aesthetic, be bold, yet fun! We will printing the posters, so we will need for them to be at high resolution and ready to send to print.

Target Market(s)

Students, Parents, and Community members

Industry/Entity Type

School

Font styles to use
Sans Serif

Colors
33a6d7
fabb78
9d9d9d
ffffff
1b1b1b
33b8a4

Requirements
Must have
• Bright Tide
• Birch & Lantern Spring Fair 2018
• Friday, May 18th
• 5:00-9:00pm
• Tickets Will Be Available at Select Pick up & Drop Off Times
• Come Enjoy a Futuristic Evening of Food, Music, Entertainment, & Fun!
Nice to have
• We’d love to see a bold and graphic poster with a futuristic feel!
• See the sample image below from previous event poster and additional images for mood and inspiration. Would love to see metallics (silver or metallic colors)

```html
<!DOCTYPE html>
<html lang="en">
<head>
<meta charset="utf-8">
<title>Bright Tide — Birch &amp; Lantern Spring Fair 2018</title>
<link href="https://fonts.googleapis.com/css2?family=Audiowide&family=Orbitron:wght@700;800&family=Cinzel:wght@400&display=swap" rel="stylesheet">
<style>
  :root {
    --ink: #1b1b1b;
    --ink-deep: #121416;
    --teal: #33b8a4;
    --sky: #33a6d7;
    --silver: #9d9d9d;
    --white: #ffffff;
  }
  html, body {
    margin: 0;
    padding: 0;
    overflow: hidden;
    background: var(--ink);
  }
  .poster {
    position: relative;
    width: 848px;
    height: 1200px;
    overflow: hidden;
    background: radial-gradient(ellipse at 50% 45%, #2a2e31 0%, var(--ink) 55%, var(--ink-deep) 100%);
    font-family: "Orbitron", sans-serif;
    color: var(--white);
  }
  .texture {
    position: absolute;
    inset: 0;
    background: linear-gradient(180deg, rgba(60,64,66,0.35) 0%, rgba(20,22,24,0.2) 60%, rgba(40,44,46,0.3) 100%);
  }
  .circuit-glow {
    position: absolute;
    border-radius: 50%;
  }
  .circuit-glow--top {
    left: 110px; top: 150px; width: 420px; height: 260px;
    background: radial-gradient(ellipse at 50% 50%, rgba(51,184,164,0.45) 0%, rgba(51,166,215,0.18) 45%, rgba(0,0,0,0) 72%);
  }
  .circuit-glow--bottom {
    left: 40px; top: 820px; width: 780px; height: 420px;
    background: radial-gradient(ellipse at 50% 55%, rgba(51,184,164,0.42) 0%, rgba(51,166,215,0.16) 45%, rgba(0,0,0,0) 72%);
  }
  .circuit-glow--core {
    left: 80px; top: 270px; width: 690px; height: 690px;
    background: radial-gradient(circle at 50% 50%, rgba(51,166,215,0.28) 0%, rgba(51,184,164,0.12) 55%, rgba(0,0,0,0) 75%);
  }
  .ring {
    position: absolute;
    left: 0; top: 0;
    width: 848px; height: 1200px;
  }
  .title {
    position: absolute;
    left: 0; right: 0; top: 30px;
    margin: 0;
    text-align: center;
    font-family: "Audiowide", sans-serif;
    font-weight: 400;
    line-height: 1;
    text-transform: uppercase;
  }
  .title__small {
    display: block;
    font-size: 34px;
    color: var(--teal);
    letter-spacing: 1px;
  }
  .title__large {
    display: inline-block;
    margin-top: 6px;
    font-size: 86px;
    letter-spacing: 1px;
    background: linear-gradient(90deg, var(--teal) 0%, var(--teal) 30%, var(--white) 72%);
    -webkit-background-clip: text;
    background-clip: text;
    color: transparent;
  }
  .details {
    position: absolute;
    left: 0; right: 0; top: 436px;
    text-align: center;
    text-transform: uppercase;
    font-style: italic;
  }
  .details p { margin: 0; line-height: 1.2; }
  .details__event { font-size: 23px; font-weight: 700; letter-spacing: 1px; }
  .details__date { font-size: 38px; font-weight: 800; letter-spacing: 1px; margin-top: 8px; }
  .details__time { font-size: 33px; font-weight: 800; letter-spacing: 1px; margin-top: 6px; }
  .details__tickets { font-size: 24px; font-weight: 800; margin-top: 12px; line-height: 1.45; }
  .tagline {
    position: absolute;
    left: 0; right: 0; top: 1110px;
    display: flex;
    align-items: center;
    gap: 12px;
    font-family: "Cinzel", serif;
    font-size: 14.5px;
    letter-spacing: 0.6px;
    text-transform: uppercase;
    white-space: nowrap;
  }
  .tagline::before, .tagline::after {
    content: "";
    flex: 1;
    height: 1px;
    background: var(--white);
  }
</style>
</head>
<body>
<main class="poster">
  <div class="texture" role="img" aria-label="Dark halftone dot texture across the background"></div>
  <div class="circuit-glow circuit-glow--top" role="img" aria-label="Glowing teal circuit-style arcs"></div>
  <div class="circuit-glow circuit-glow--core" role="img" aria-label="Teal technical circle pattern inside the ring"></div>
  <div class="circuit-glow circuit-glow--bottom" role="img" aria-label="Large glowing teal circuit dial at the base"></div>

  <svg class="ring" viewBox="0 0 848 1200" aria-hidden="true">
    <defs>
      <linearGradient id="metal" x1="0" y1="0" x2="1" y2="1">
        <stop offset="0" stop-color="#e8e8e8"/>
        <stop offset="0.25" stop-color="#9d9d9d"/>
        <stop offset="0.5" stop-color="#f4f4f4"/>
        <stop offset="0.75" stop-color="#7e7e7e"/>
        <stop offset="1" stop-color="#d6d6d6"/>
      </linearGradient>
      <radialGradient id="rivet-fill" cx="0.4" cy="0.35" r="0.7">
        <stop offset="0" stop-color="#ffffff"/>
        <stop offset="0.5" stop-color="#9d9d9d"/>
        <stop offset="1" stop-color="#4a4a4a"/>
      </radialGradient>
      <circle id="rivet" cx="425" cy="244" r="8.5" fill="url(#rivet-fill)" stroke="#2a2a2a" stroke-width="1"/>
    </defs>
    <circle cx="425" cy="611" r="388" fill="none" stroke="#0f1112" stroke-width="3"/>
    <circle cx="425" cy="611" r="367" fill="none" stroke="url(#metal)" stroke-width="40"/>
    <circle cx="425" cy="611" r="346" fill="none" stroke="#0f1112" stroke-width="3"/>
    <g class="rivets">
      <use href="#rivet"/>
      <use href="#rivet" transform="rotate(12.857 425 611)"/>
      <use href="#rivet" transform="rotate(25.714 425 611)"/>
      <use href="#rivet" transform="rotate(38.571 425 611)"/>
      <use href="#rivet" transform="rotate(51.429 425 611)"/>
      <use href="#rivet" transform="rotate(64.286 425 611)"/>
      <use href="#rivet" transform="rotate(77.143 425 611)"/>
      <use href="#rivet" transform="rotate(90 425 611)"/>
      <use href="#rivet" transform="rotate(102.857 425 611)"/>
      <use href="#rivet" transform="rotate(115.714 425 611)"/>
      <use href="#rivet" transform="rotate(128.571 425 611)"/>
      <use href="#rivet" transform="rotate(141.429 425 611)"/>
      <use href="#rivet" transform="rotate(154.286 425 611)"/>
      <use href="#rivet" transform="rotate(167.143 425 611)"/>
      <use href="#rivet" transform="rotate(180 425 611)"/>
      <use href="#rivet" transform="rotate(192.857 425 611)"/>
      <use href="#rivet" transform="rotate(205.714 425 611)"/>
      <use href="#rivet" transform="rotate(218.571 425 611)"/>
      <use href="#rivet" transform="rotate(231.429 425 611)"/>
      <use href="#rivet" transform="rotate(244.286 425 611)"/>
      <use href="#rivet" transform="rotate(257.143 425 611)"/>
      <use href="#rivet" transform="rotate(270 425 611)"/>
      <use href="#rivet" transform="rotate(282.857 425 611)"/>
      <use href="#rivet" transform="rotate(295.714 425 611)"/>
      <use href="#rivet" transform="rotate(308.571 425 611)"/>
      <use href="#rivet" transform="rotate(321.429 425 611)"/>
      <use href="#rivet" transform="rotate(334.286 425 611)"/>
      <use href="#rivet" transform="rotate(347.143 425 611)"/>
    </g>
  </svg>

  <h1 class="title">
    <span class="title__small">Bright</span>
    <span class="title__large">Tide</span>
  </h1>

  <section class="details">
    <p class="details__event">Birch &amp; Lantern Spring Fair 2018</p>
    <p class="details__date">Friday, May 18th</p>
    <p class="details__time">5:00-9:00pm</p>
    <p class="details__tickets">Tickets will be<br>available at select pick up<br>&amp; drop off times</p>
  </section>

  <p class="tagline">Come enjoy a futuristic evening of food, music, entertainment, &amp; fun!</p>
</main>
</body>
</html>
```